Corporate Design für Kunsthandwerk
Zielgruppe
Wir machen Kunsthandwerk mit Schwerpunkt Liquidmetall und wollen ein entsprechendes Logo dazu. Unsere Zielgruppe liegt im Höherem Preissigment
Aufgabenstellung
Wir suchen ein Design das eine moderne Firma im Kunsthandwerk wiederspiegelt, die auf Spezielle Designs im Bereich Interieur und Exterieur spezialisiert ist.

```html
<!DOCTYPE html>
<html lang="de">
<head>
<meta charset="utf-8">
<title>ORVANT – Corporate Design</title>
<link rel="stylesheet" href="https://fonts.googleapis.com/css2?family=Open+Sans:wght@400;600;700&display=swap">
<style>
:root{
  --bg:#ebebeb;
  --paper:#fafafa;
  --umber:#524846;
  --ink:#4b4240;
  --gold:#c9a23f;
  --text:#6a6361;
  --shadow:0 1px 3px rgba(0,0,0,.22);
}
*{box-sizing:border-box;margin:0;padding:0}
html,body{width:698px;height:1200px;overflow:hidden;background:var(--bg)}
body{position:relative;font-family:"Open Sans",Arial,sans-serif;color:var(--ink)}
.abs{position:absolute}

/* brand name */
.brand{position:absolute;display:flex;align-items:center;gap:3px;font-family:"Open Sans",Arial,sans-serif;font-weight:600;letter-spacing:.14em;line-height:1;white-space:nowrap;color:var(--ink)}
.brand .mark{display:inline-block;background:var(--gold)}
.brand--gold{color:var(--gold)}

/* business cards */
.card{position:absolute;width:159px;height:91px;box-shadow:var(--shadow);overflow:hidden}
.card--back{background:var(--umber)}
.card--back .brand{font-size:15px;left:0;right:0;top:38px;justify-content:center}
.card--back .mark{width:4px;height:4px}
.card--front{background:var(--paper)}
.card--front .tagline{position:absolute;left:10px;top:24px;font-size:4.6px;color:var(--ink)}
.card--front .brand{font-size:13px;right:12px;top:20px}
.card--front .mark{width:3px;height:3px}
.card__address,.card__contact{position:absolute;top:61px;font-size:3.5px;line-height:4.1px;color:var(--ink)}
.card__address{left:11px}
.card__contact{left:99px}
.card__band{position:absolute;left:0;bottom:0;width:159px;height:9px}

/* letterheads */
.letter{position:absolute;top:393px;width:247px;height:352px;background:var(--paper);box-shadow:var(--shadow)}
.letter .brand{font-size:10px;top:21px}
.letter .mark{width:2.4px;height:2.4px}
.letter__sender{position:absolute;left:19px;top:53px;font-size:2.7px;color:var(--ink);border-bottom:.4px solid var(--ink);padding-bottom:1px}
.recipient{position:absolute;left:27px;top:75px;width:192px}
.recipient__name{font-size:5.2px;font-weight:600;color:#2f2a29;margin-bottom:2.5px}
.recipient__line{font-size:3.6px;line-height:5.3px;color:var(--text)}
.recipient__date{position:absolute;right:0;bottom:0;font-size:3.6px;color:var(--text)}
.letter__body{position:absolute;left:27px;top:116px;width:192px}
.letter__body p{font-size:3.5px;line-height:5.35px;color:var(--text);text-align:justify;margin-bottom:5.5px}
.signature{position:absolute;left:27px;top:252px}
.signature__script{width:46px;height:9px;background:linear-gradient(90deg,rgba(60,55,54,.35),rgba(60,55,54,.15));border-radius:3px}
.signature__name{font-size:4.8px;font-weight:600;color:#2f2a29;margin-top:2px}
.signature__role{font-size:3.6px;color:var(--text);margin-top:1px}
.fold{position:absolute;left:0;width:6px;height:.5px;background:#555}
.letter__footer{position:absolute;left:20px;right:20px;top:329px;border-top:.6px solid #333;padding-top:3px;display:flex;justify-content:space-between}
.letter__footer div{font-size:2.3px;line-height:3px;color:#333;padding:0 3px;border-right:.5px solid #333}
.letter__footer div:last-child{border-right:none}

/* envelopes */
.envelope{position:absolute;left:201px;width:296px;height:154px;background:linear-gradient(135deg,#fbfbfb 0%,#f1f1f1 55%,#fafafa 100%);box-shadow:var(--shadow);overflow:hidden}
.envelope .brand{font-size:10px}
.envelope .mark{width:2.4px;height:2.4px}
.envelope__window{position:absolute;left:21px;top:82px;width:117px;height:54px;background:#e6e6e6;border-radius:3px}
.envelope__flap{position:absolute;left:0;top:0}
</style>
</head>
<body>

<!-- business cards -->
<div class="card card--back" style="left:97px;top:67px"><div class="brand brand--gold">ORVANT<span class="mark"></span></div></div>
<div class="card card--front" style="left:269px;top:67px">
  <div class="tagline">Entwurf Galerie</div>
  <div class="brand">ORVANT<span class="mark"></span></div>
  <div class="card__address">ENTWURFGALERIE<br>Birkenweg 7<br>D-90762 Fürth</div>
  <div class="card__contact">Tel: 089 / 00 00 00 - 00<br>Fax: 089 / 00 00 00 - 0000<br>Mobil: 0178 / 000 00 00<br>info@entwurfgalerie.de</div>
  <svg class="card__band" viewBox="0 0 159 9"><rect x="0" y="6.5" width="84" height="2.5" fill="#c9a23f"/><polygon points="80,9 89,0 159,0 159,9" fill="#524846"/></svg>
</div>
<div class="card card--back" style="left:441px;top:67px"><div class="brand brand--gold">ORVANT<span class="mark"></span></div></div>

<div class="card card--front" style="left:97px;top:171px">
  <div class="tagline">Entwurf Galerie</div>
  <div class="brand">ORVANT<span class="mark"></span></div>
  <div class="card__address">ENTWURFGALERIE<br>Birkenweg 7<br>D-90762 Fürth</div>
  <div class="card__contact">Tel: 089 / 00 00 00 - 00<br>Fax: 089 / 00 00 00 - 0000<br>Mobil: 0178 / 000 00 00<br>info@entwurfgalerie.de</div>
  <svg class="card__band" viewBox="0 0 159 9"><rect x="0" y="6.5" width="84" height="2.5" fill="#c9a23f"/><polygon points="80,9 89,0 159,0 159,9" fill="#524846"/></svg>
</div>
<div class="card card--back" style="left:269px;top:171px"><div class="brand brand--gold">ORVANT<span class="mark"></span></div></div>
<div class="card card--front" style="left:441px;top:171px">
  <div class="tagline">Entwurf Galerie</div>
  <div class="brand">ORVANT<span class="mark"></span></div>
  <div class="card__address">ENTWURFGALERIE<br>Birkenweg 7<br>D-90762 Fürth</div>
  <div class="card__contact">Tel: 089 / 00 00 00 - 00<br>Fax: 089 / 00 00 00 - 0000<br>Mobil: 0178 / 000 00 00<br>info@entwurfgalerie.de</div>
  <svg class="card__band" viewBox="0 0 159 9"><rect x="0" y="6.5" width="84" height="2.5" fill="#c9a23f"/><polygon points="80,9 89,0 159,0 159,9" fill="#524846"/></svg>
</div>

<div class="card card--back" style="left:97px;top:275px"><div class="brand brand--gold">ORVANT<span class="mark"></span></div></div>
<div class="card card--front" style="left:269px;top:275px">
  <div class="tagline">Entwurf Galerie</div>
  <div class="brand">ORVANT<span class="mark"></span></div>
  <div class="card__address">ENTWURFGALERIE<br>Birkenweg 7<br>D-90762 Fürth</div>
  <div class="card__contact">Tel: 089 / 00 00 00 - 00<br>Fax: 089 / 00 00 00 - 0000<br>Mobil: 0178 / 000 00 00<br>info@entwurfgalerie.de</div>
  <svg class="card__band" viewBox="0 0 159 9"><rect x="0" y="6.5" width="84" height="2.5" fill="#c9a23f"/><polygon points="80,9 89,0 159,0 159,9" fill="#524846"/></svg>
</div>
<div class="card card--back" style="left:441px;top:275px"><div class="brand brand--gold">ORVANT<span class="mark"></span></div></div>

<!-- letterhead, first page -->
<div class="letter" style="left:99px">
  <div class="brand" style="left:25px">ORVANT<span class="mark"></span></div>
  <div class="letter__sender">ENTWURFGALERIE &nbsp;|&nbsp; Birkenweg 7 &nbsp;|&nbsp; D-90762 Fürth</div>
  <div class="recipient">
    <div class="recipient__name">Name Surname</div>
    <div class="recipient__line">Senior Executive</div>
    <div class="recipient__line">Address goes here. Street, City, Country</div>
    <div class="recipient__line">contact@yourmail.com</div>
    <div class="recipient__line">000-987-654-321</div>
    <div class="recipient__date">Date, 10 September, 2030</div>
  </div>
  <div class="letter__body">
    <p>Lorem ipsum dolor sit amet, consectetur adipisicing elit, sed do eiusmod tempor incididunt ut labore et dolore magna aliqua. Ut enim ad minim veniam, quis nostrud exercitation ullamco laboris nisi ut aliquip ex ea commodo consequat. Duis aute irure dolor in reprehenderit in voluptate velit esse cillum dolore eu fugiat nulla pariatur. Excepteur sint occaecat cupidatat non proident, sunt in culpa qui officia deserunt mollit anim id est laborum. Sed ut perspiciatis unde omnis iste natus error sit voluptatem accusantium doloremque laudantium, totam rem aperiam, eaque ipsa quae ab illo inventore veritatis et quasi architecto beatae vitae dicta sunt explicabo. Nemo enim ipsam voluptatem quia voluptas sit aspernatur aut odit aut fugit, sed quia consequuntur magni dolores eos qui ratione voluptatem sequi nesciunt. Neque porro voluptatem sequi nesciunt. Nemo enim ipsam voluptatem quia voluptas.</p>
    <p>Lorem ipsum dolor sit amet, consectetur adipisicing elit, sed do eiusmod tempor incididunt ut labore et dolore magna aliqua. Ut enim ad minim veniam, quis nostrud exercitation ullamco laboris nisi ut aliquip ex ea commodo consequat. Duis aute irure dolor in reprehenderit in voluptate velit esse cillum dolore eu fugiat nulla pariatur. Excepteur sint occaecat cupidatat non proident, sunt in culpa qui officia deserunt mollit anim id est laborum. Sed ut perspiciatis unde omnis iste natus error sit voluptatem accusantium doloremque laudantium, totam rem aperiam, eaque ipsa quae ab illo inventore veritatis et quasi architecto beatae vitae dicta sunt explicabo. Nemo enim ipsam voluptatem quia voluptas sit aspernatur aut odit aut.</p>
    <p>Lorem ipsum dolor sit amet, consectetur adipisicing elit, sed do eiusmod tempor incididunt ut labore et dolore magna aliqua. Ut enim ad minim veniam, quis nostrud exercitation ullamco laboris nisi ut aliquip ex ea commodo consequat.</p>
  </div>
  <div class="signature">
    <div class="signature__script" role="img" aria-label="Handschriftliche Unterschrift"></div>
    <div class="signature__name">NAME SURNAME</div>
    <div class="signature__role">General Manager</div>
  </div>
  <div class="fold" style="top:124px"></div>
  <div class="fold" style="top:176px"></div>
  <div class="fold" style="top:250px"></div>
  <div class="letter__footer">
    <div>Geschäftsführung:<br>Entwurfgalerie.de<br>Sitz der Gesellschaft:</div>
    <div>Amtsgericht Fürth HRB-Nr. 0000<br>EORI-Nr. DE 000 0000<br>Ust-IdNr.: DE000 000 000<br>Steuer-Nr. 000/000/00000</div>
    <div>Ostbank Fürth<br>IBAN DE00 0000 0000 0000 0000 00<br>BIC OSTBDEMMXXX</div>
    <div>Talsparkasse Erlangen<br>IBAN DE00 0000 0000 0000 0000 00<br>BIC TALSDE1KMS</div>
  </div>
</div>

<!-- letterhead, second page -->
<div class="letter" style="left:355px">
  <div class="brand" style="right:19px">ORVANT<span class="mark"></span></div>
  <div class="recipient">
    <div class="recipient__name">Name Surname</div>
    <div class="recipient__line">Senior Executive</div>
    <div class="recipient__line">Address goes here. Street, City, Country</div>
    <div class="recipient__line">contact@yourmail.com</div>
    <div class="recipient__line">000-987-654-321</div>
    <div class="recipient__date">Date, 10 September, 2030</div>
  </div>
  <div class="letter__body">
    <p>Lorem ipsum dolor sit amet, consectetur adipisicing elit, sed do eiusmod tempor incididunt ut labore et dolore magna aliqua. Ut enim ad minim veniam, quis nostrud exercitation ullamco laboris nisi ut aliquip ex ea commodo consequat. Duis aute irure dolor in reprehenderit in voluptate velit esse cillum dolore eu fugiat nulla pariatur. Excepteur sint occaecat cupidatat non proident, sunt in culpa qui officia deserunt mollit anim id est laborum. Sed ut perspiciatis unde omnis iste natus error sit voluptatem accusantium doloremque laudantium, totam rem aperiam, eaque ipsa quae ab illo inventore veritatis et quasi architecto beatae vitae dicta sunt explicabo. Nemo enim ipsam voluptatem quia voluptas sit aspernatur aut odit aut fugit, sed quia consequuntur magni dolores eos qui ratione voluptatem sequi nesciunt. Neque porro voluptatem sequi nesciunt. Nemo enim ipsam voluptatem quia voluptas.</p>
    <p>Lorem ipsum dolor sit amet, consectetur adipisicing elit, sed do eiusmod tempor incididunt ut labore et dolore magna aliqua. Ut enim ad minim veniam, quis nostrud exercitation ullamco laboris nisi ut aliquip ex ea commodo consequat. Duis aute irure dolor in reprehenderit in voluptate velit esse cillum dolore eu fugiat nulla pariatur. Excepteur sint occaecat cupidatat non proident, sunt in culpa qui officia deserunt mollit anim id est laborum. Sed ut perspiciatis unde omnis iste natus error sit voluptatem accusantium doloremque laudantium, totam rem aperiam, eaque ipsa quae ab illo inventore veritatis et quasi architecto beatae vitae dicta sunt explicabo. Nemo enim ipsam voluptatem quia voluptas sit aspernatur aut odit aut.</p>
    <p>Lorem ipsum dolor sit amet, consectetur adipisicing elit, sed do eiusmod tempor incididunt ut labore et dolore magna aliqua. Ut enim ad minim veniam, quis nostrud exercitation ullamco laboris nisi ut aliquip ex ea commodo consequat.</p>
  </div>
  <div class="signature">
    <div class="signature__script" role="img" aria-label="Handschriftliche Unterschrift"></div>
    <div class="signature__name">NAME SURNAME</div>
    <div class="signature__role">General Manager</div>
  </div>
  <div class="fold" style="top:113px"></div>
  <div class="fold" style="top:165px"></div>
  <div class="fold" style="top:239px"></div>
</div>

<!-- envelope front -->
<div class="envelope" style="top:770px">
  <div class="brand" style="left:28px;top:41px">ORVANT<span class="mark"></span></div>
  <div class="envelope__window"></div>
</div>

<!-- envelope back -->
<div class="envelope" style="top:943px">
  <svg class="envelope__flap" width="296" height="47" viewBox="0 0 296 47"><path d="M0 0 H296 L280 30 Q272 46 254 46 H42 Q24 46 16 30 Z" fill="#524846"/></svg>
  <div class="brand" style="left:229px;top:125px">ORVANT<span class="mark"></span></div>
</div>

</body>
</html>
```